Office brochure for chronic pain doctor

I need an brochure for my office, and since I want to be able to mail the brochure, I think trifold would be the best size. I treat patients with chronic head and neck pain, as well as sleep apnea. I treat all of the following:

1. headaches
2. myofascial pain, which is a fancy way of saying muscle pain
3. neuropathic pain, which is a fancy way of saying nerve pain
4. TMJ, which stands for the temporomandibular joint (jaw joint)
5. obstructive sleep apnea

The colors will be based on my logo on my website, which you can see at www.BrightJPR.net, and you can learn more about what I do at my website. JPR stands for orofacial pain, which is a speciality training within the field of dentistry but I do not treat teeth. I have high resolution graphics for the brochure so I need someone with an artistic eye to design and lay out the brochure.

The logo colors are:
Purple 9e80bb
Pink f6b1d0
Blue 0f4b8f
Updates

I had a request for the logo in a .ai or .pdf format, which I have just uploaded. Please let me know if you have any other requests. Thank you, Dale

Target Market(s)

80% female, 20% male. I am in an upscale area of Los Angeles called Beverly Hills but I will see a patient from any area around Los Angeles or from any area in the world.

Industry/Entity Type

Training

Colors
6b449b
e567a6
0355a3

Requirements
Must have
• I want a small section of the brochure to feature each of the five areas I treat, and I have included an image to place in each of the five sections. A small section should include a short bio of me, which you can condense from www.brightjpr.net/dale. The brochure must appeal to women since 80% of my patients are female but I don't want to completely ignore men. Most of the pain patients are female, and most of the sleep apnea patients are male.

Here are the colors in my logo
Purple 9e80bb
Pink f6b1d0
Blue 0f4b8f
Should not have
• Anything related to teeth or dentistry.
No decorative or script fonts.

```html
<!DOCTYPE html>
<html lang="en">
<head>
<meta charset="utf-8">
<title>Trifold Brochure – Head Pain and Sleep Apnea</title>
<link href="https://fonts.googleapis.com/css2?family=Roboto+Condensed:wght@400;700&display=swap" rel="stylesheet">
<style>
:root{
  --stage:#cccccc;
  --blue:#0f4b8f;
  --purple:#9e80bb;
  --pink:#f6b1d0;
  --sky:#aebde6;
  --ink:#222222;
  --white:#ffffff;
  --rule:#333333;
}
*{box-sizing:border-box;margin:0;padding:0}
html,body{width:1200px;height:1002px;overflow:hidden;background:var(--stage);
  font-family:"Roboto Condensed",Arial,sans-serif;color:var(--ink)}
.canvas{position:relative;width:1200px;height:1002px}
.sheet{position:absolute;left:310px;width:600px;border:1px solid var(--rule);overflow:hidden}
.sheet--outside{top:20px;height:464px}
.sheet--inside{top:516px;height:463px}
.panel{position:absolute;top:0;width:200px;height:100%}
.panel + .panel{border-left:1px solid var(--rule)}
.p1{left:0}.p2{left:200px}.p3{left:400px}
.block{position:absolute;left:0;width:200px}
.block--blue{background:var(--blue);color:var(--white)}
.block--purple{background:var(--purple);color:var(--white)}
.block--pink{background:var(--pink);color:var(--white)}
.art{position:absolute;left:0;width:200px}
.heading{font-weight:400;font-size:19px;line-height:1.1;margin-bottom:8px;white-space:nowrap}
.body{font-size:7.4px;line-height:1.45}
.notch{position:absolute;width:0;height:0;left:88px;border-left:14px solid transparent;border-right:14px solid transparent;z-index:2}
.notch--down-blue{border-top:14px solid var(--blue)}
.notch--down-purple{border-top:14px solid var(--purple)}
.notch--up-pink{border-bottom:14px solid var(--pink)}
.notch--up-blue{border-bottom:14px solid var(--blue)}
.label{position:absolute;font-weight:700;font-size:15px;color:#222}
.label--small{font-size:11px}
/* back panel */
.back{background:var(--sky);text-align:center}
.portrait{position:absolute;left:56px;top:20px;width:89px;height:87px;border-radius:3px;
  background:linear-gradient(160deg,#6f7d8a,#c9cfd6 60%,#eef0f2)}
.doc-name{position:absolute;top:113px;left:0;width:200px;font-weight:700;font-size:7.5px}
.doc-cred{position:absolute;top:123px;left:0;width:200px;font-size:5.2px;line-height:1.35;font-weight:700}
.bio{position:absolute;top:147px;left:18px;width:168px;text-align:left;font-size:6.6px;line-height:1.45}
.brand{position:absolute;left:0;width:200px;display:flex;align-items:center;justify-content:center;gap:5px;color:var(--blue);font-weight:700}
.brand-mark{display:inline-block;background:var(--purple)}
.address{position:absolute;top:368px;left:0;width:200px;font-size:6.6px;line-height:1.5}
.web{position:absolute;left:0;width:200px;text-align:center;font-weight:700;font-size:5.6px}
/* front panel */
.front{background:var(--sky)}
.tile{position:absolute;width:89px;height:87px;border-radius:4px;border:1px solid #8a8a8a}
.title-front{position:absolute;top:307px;left:0;width:200px;text-align:center;font-weight:700;font-size:14px;line-height:1.4;color:#444}
</style>
</head>
<body>
<div class="canvas">

  <section class="sheet sheet--outside" aria-label="Outside of brochure">
    <div class="panel p1">
      <div class="block block--blue" style="top:0;height:130px;padding:12px 18px">
        <h2 class="heading">What is TMJD?</h2>
        <p class="body">Temporomandibular joint disorder, also known as TMJ, TMD, or TMJD, is a general term covering any disorder causing inflammation of the temporomandibular joint, which connects the skull to the mandible. There are a number of conditions that can cause pain in the jaw joint and the muscles involved in the closing and opening of the jaw.</p>
      </div>
      <div class="notch notch--down-blue" style="top:130px"></div>
      <div class="art" role="img" aria-label="Illustration of the jaw joint and chewing muscles" style="top:130px;height:122px;background:linear-gradient(120deg,#e9e2d6,#b8493e 45%,#e6c9a4 80%)"></div>
      <div class="block block--purple" style="top:252px;height:103px;padding:8px 18px">
        <h2 class="heading">What is Sleep Apnea?</h2>
        <p class="body">Sleep apnea is a common sleeping disorder marked by shallow breathing, pauses in breath and labored breathing punctuated by gasping or snoring sounds. Pauses of breath can last from several seconds up to minutes and can happen from five to thirty times or more per hour.</p>
      </div>
      <div class="notch notch--down-purple" style="top:355px"></div>
      <div class="art" role="img" aria-label="Illustration of the airway of a sleeping person" style="top:355px;height:110px;background:linear-gradient(100deg,#f3e5dc,#b85a4c 40%,#f1dccf 75%)"></div>
    </div>

    <div class="panel p2 back">
      <div class="portrait" role="img" aria-label="Portrait photo of the doctor"></div>
      <div class="doc-name">Dr. Dale Whitcombe</div>
      <div class="doc-cred">DDS, MBA, Diplomate National Board of Facial Pain<br>Lakemont Facial Pain Doctor</div>
      <p class="bio">Do you like change, which is a large part of life today? I do so needless to say, I have had an interesting career. I was born in Lincoln Falls and moved to Westbrook in 1965, and then to Oakvale in 1966, which is where I spent my childhood. I was a "valley boy" having attended Oakvale Elementary, Maple Ridge Junior High in Westbrook, and Cedar Park High School in Cedar Park. After high school, I attended Harlow University in Bayport, and was constantly asked why I moved away from home. Harlow was a fantastic experience but I knew I had more education ahead of me since I had wanted to be a dentist since my early teens. I attended dental school at Westmont College of Dentistry from 1981-1985, and started my career in private practice a few months after graduation.</p>
      <div class="brand" style="top:318px;font-size:8px"><span class="brand-mark" style="width:12px;height:12px"></span>Harborview Head Pain</div>
      <div class="address">4820 Linden Court, Suite 210<br>Lakemont, California 90417<br>Ph. 555.014.2271 • Fx. 555.014.2290</div>
      <div class="web" style="top:425px">www.harborviewheadpain.com</div>
    </div>

    <div class="panel p3 front">
      <div class="tile" style="left:8px;top:18px;background:linear-gradient(135deg,#f2e3d8,#d8332e 55%,#8a5a3e)" role="img" aria-label="Illustration of headache pain area on forehead"></div>
      <div class="tile" style="left:102px;top:18px;background:var(--pink)"></div>
      <div class="tile" style="left:8px;top:108px;background:var(--purple)"></div>
      <div class="tile" style="left:102px;top:108px;background:linear-gradient(135deg,#c9614f,#efe1d2 60%,#b8493e)" role="img" aria-label="Illustration of facial muscles with trigger points"></div>
      <div class="tile" style="left:8px;top:198px;background:linear-gradient(120deg,#e9e2d6,#b8493e 50%,#e6c9a4)" role="img" aria-label="Illustration of the jaw joint"></div>
      <div class="tile" style="left:102px;top:198px;background:var(--blue)"></div>
      <h1 class="title-front">Caring for Head Pain<br>and Sleep Apnea</h1>
      <div class="brand" style="top:363px;font-size:12px"><span class="brand-mark" style="width:18px;height:18px"></span>Harborview Head Pain</div>
      <div class="web" style="top:429px">www.harborviewheadpain.com</div>
    </div>
  </section>

  <span class="label" style="left:922px;top:293px">OUTSIDE PAGE</span>
  <span class="label label--small" style="left:576px;top:489px">BACK PAGE</span>
  <span class="label label--small" style="left:777px;top:487px">FRONT PAGE</span>

  <section class="sheet sheet--inside" aria-label="Inside of brochure">
    <div class="panel p1">
      <div class="art" role="img" aria-label="Illustration of a woman with headache pain across the forehead and eye" style="top:0;height:232px;background:linear-gradient(135deg,#7a4a30,#f1dccd 35%,#d8302b 60%,#f0dccd 85%)"></div>
      <div class="notch notch--up-pink" style="top:218px"></div>
      <div class="block block--pink" style="top:232px;height:231px;padding:30px 18px">
        <h2 class="heading">What is a Headache?</h2>
        <p class="body" style="margin-top:14px">A headache is an ache or pain occurring anywhere in the face, neck or head. Headache pain is experienced through pain-sensitive structures around the head and neck including blood vessels, nerves, muscles and tissues including the eyes, ears and sinuses. Headaches can range across the intensity spectrum from mild, tolerable pain to severe pain that prohibits daily activities. Headaches are one of the most commonly experienced causes of pain. They can be occasional, recurrent or chronic in frequency.</p>
      </div>
    </div>

    <div class="panel p2">
      <div class="block block--purple" style="top:0;height:229px;padding:40px 16px 0">
        <p class="body">Chronic myofascial pain (CMP) is a chronic pain disease characterized by trigger points in the musculature causing pain in distinct areas of the body. Pain symptoms of CMP can be severe and debilitating. While much of the underlying mechanics of myofascial pain is not clearly understood, research suggests that symptoms are derived from the existence of trigger points within muscles, which are activated by injury or repetitive strain to muscles. It is generally understood that while one trigger point may be responsible for an experience of myofascial pain, it is more commonly a network of several trigger points that contribute to pain in a given region.</p>
        <h2 class="heading" style="position:absolute;top:204px;left:14px;font-size:17.5px">What is Myofascial Pain?</h2>
      </div>
      <div class="notch notch--down-purple" style="top:229px"></div>
      <div class="art" role="img" aria-label="Illustration of facial and neck muscles with trigger points" style="top:229px;height:234px;background:linear-gradient(135deg,#8c3a2e,#c9614f 40%,#f0e6da 60%,#b8493e)"></div>
    </div>

    <div class="panel p3">
      <div class="art" role="img" aria-label="Facial nerve diagram showing three nerve branch regions and pain percentages" style="top:0;height:232px;background:linear-gradient(180deg,#b98a64,#f2dccb 30%,#eccab6 80%,#d9a896)"></div>
      <div class="notch notch--up-blue" style="top:218px"></div>
      <div class="block block--blue" style="top:232px;height:231px;padding:30px 24px">
        <h2 class="heading" style="font-size:17px">Neuropathic Pain</h2>
        <p class="body">Various orofacial neuropathies derive from a number of causes. Depending on the symptoms experienced, the diagnostic process may be different. For the three most common orofacial neuropathic pain conditions, diagnostic procedures may include the following tests, examinations and considerations.</p>
        <p class="body" style="margin-top:8px">As with any diagnostic process, a doctor will take a full medical history and description of symptoms, perform a physical exam and any necessary tests or scan.</p>
      </div>
    </div>
  </section>

  <span class="label" style="left:930px;top:738px">INSIDE PAGE</span>
</div>
</body>
</html>
```